Retail Sign for Houseplant Campaign

Please make Portrait style not landscape Sign will measure 3 to 4 foot tall by 22.2inches and place on rolling racks of houseplants for a retail promotion in The Yard Outlet. The theme of the promotion will be "Bring your home to life with Houseplants!" Selling points which should be on the sign are Houseplants * improve your mood * reduce fatigue * improve focus. Please put signage in landscape format and include yard outlet and verdant fields logo.
Updates

Just recovered from covid. Im sorry for the delay

Target Market(s)

People who love plants

Industry/Entity Type

Retail

Colors
00AB8E
00BBA5
67D7C9
C6EFE9
E9F9F6
59FF00
82FF00
B8FF75
E3FFCB
F4FFEA
FFF300
FFF600
FEFA6F
FFFEC7
FFFEE8
FFC000
F8CF3A
FAE287
FDF2CF
FEFAEE

Requirements
Must have
• Must feel energetic and encourage people to buy plants. Should include 1-2 photos and the selling points listed

```html
<!DOCTYPE html>
<html lang="en">
<head>
<meta charset="utf-8">
<title>Bring your Home to life with Houseplants</title>
<link rel="stylesheet" href="https://fonts.googleapis.com/css2?family=Kaushan+Script&family=Quicksand:wght@400;500&display=swap">
<style>
  :root {
    --backdrop: #ececec;
    --paper: #ffffff;
    --ink: #585858;
    --ink-dark: #1e1e1e;
    --sun-yellow: #ece935;
    --lime-rule: #c8dd20;
    --script: "Kaushan Script", cursive;
    --sans: "Quicksand", sans-serif;
  }
  * { margin: 0; padding: 0; box-sizing: border-box; }
  html, body {
    width: 1081px; height: 1200px; overflow: hidden;
    background: var(--backdrop);
  }
  .sign {
    position: absolute; left: 196px; top: 15px;
    width: 690px; height: 1170px;
    background: var(--paper);
    font-family: var(--sans);
    color: var(--ink);
    overflow: hidden;
  }
  .headline {
    position: absolute; left: 0; right: 0; top: 112px;
    text-align: center; font-weight: 400;
  }
  .headline .line { display: block; white-space: nowrap; }
  .headline .script { font-family: var(--script); font-weight: 400; }
  .line-one { font-size: 84px; line-height: 100px; margin-left: 30px; }
  .line-one .plain { font-family: var(--sans); font-size: 70px; margin-left: 10px; }
  .line-two { font-size: 74px; line-height: 96px; letter-spacing: -1px; margin-left: 50px; }
  .line-three { font-size: 80px; line-height: 100px; margin-left: 40px; }
  .benefit-panel {
    position: absolute; left: 142px; top: 429px;
    width: 435px; height: 615px;
    background: var(--sun-yellow);
  }
  .benefit-list {
    list-style: none;
    position: absolute; left: 0; right: 0; top: 38px;
    text-align: center;
    color: var(--ink-dark);
    font-size: 32px; font-weight: 500; line-height: 40px;
  }
  .benefit-list li { padding: 4px 0 8px; }
  .benefit-list .divider {
    display: block; width: 265px; height: 3px; margin: 0 auto; padding: 0;
    background: linear-gradient(90deg, transparent, rgba(255,255,255,.95), transparent);
  }
  .photo-person {
    position: absolute; left: 19px; top: 637px;
    width: 300px; height: 456px;
    background: linear-gradient(180deg, #7a5a44 0%, #8fa8a8 45%, #6f8f90 75%, #2b3346 100%);
    border-radius: 120px 120px 0 0;
  }
  .photo-plants {
    position: absolute; left: 250px; top: 860px;
    width: 440px; height: 233px;
    background: linear-gradient(180deg, rgba(60,130,50,.55) 0%, #3f8a36 45%, #2f6b2a 100%);
  }
  .footer-rule {
    position: absolute; left: 0; right: 0; top: 1093px;
    height: 7px; background: var(--lime-rule);
  }
  .web-address {
    position: absolute; left: 0; right: 0; top: 1114px;
    text-align: center;
    font-size: 27px; font-weight: 500; letter-spacing: 4px;
    color: var(--ink);
  }
</style>
</head>
<body>
  <main class="sign">
    <h1 class="headline">
      <span class="line line-one"><span class="script">Bring</span><span class="plain"> your</span></span>
      <span class="line line-two">Home to life with</span>
      <span class="line line-three script">Houseplants!</span>
    </h1>

    <section class="benefit-panel">
      <ul class="benefit-list">
        <li>Improve Your Mood</li>
        <li class="divider" aria-hidden="true"></li>
        <li>Reduce Fatigue</li>
        <li class="divider" aria-hidden="true"></li>
        <li>Improve Focus</li>
      </ul>
    </section>

    <div class="photo-person" role="img" aria-label="Photo of a smiling woman hugging a potted monstera plant"></div>
    <div class="photo-plants" role="img" aria-label="Photo of a row of leafy green houseplants and snake plants"></div>

    <div class="footer-rule"></div>
    <p class="web-address">www.yourwebaddress.com</p>
  </main>
</body>
</html>
```